Boutique Real Estate Brokerage looking for business card, letterhead and envelope design

We are looking for a cohesive design for our business cards, letterhead and envelopes and that mirrors our high-end homes and clientele. Cedar & Vane is being launched and designed for the marketplace of tomorrow. We grew from the #1 team in our community into a full-service firm that is going to revolutionize the traditional real estate model.

We understand that it’s more important than ever to help our clients and partners adapt to behavioral and market changes being driven by generational shifts and technological advances in society, and by combining traditional brokerage services with innovative production and marketing capabilities, we know how to do that better than anyone else.

Requirements
Must have
• business card, letterhead and envelope design - attached logo.

```html
<!DOCTYPE html>
<html lang="en">
<head>
<meta charset="utf-8">
<title>Cedar &amp; Vane Stationery</title>
<link href="https://fonts.googleapis.com/css2?family=Lato:wght@400;700&family=Montserrat:wght@700&family=Parisienne&display=swap" rel="stylesheet">
<style>
  :root{
    --navy:#1f1a4f;
    --gold:#bd8243;
    --paper:#f5f4f6;
    --ink:#3b3a4a;
    --bg:#e4e4e6;
  }
  *{margin:0;padding:0;box-sizing:border-box;}
  html,body{width:1200px;height:800px;overflow:hidden;background:var(--bg);}
  body{position:relative;font-family:'Lato',sans-serif;color:var(--ink);}
  .sheet{position:absolute;background:var(--paper);overflow:hidden;}

  .wordmark{display:flex;align-items:center;gap:6px;font-family:'Montserrat',sans-serif;font-weight:700;color:var(--navy);white-space:nowrap;letter-spacing:.02em;}
  .wordmark .mark{display:inline-block;background:var(--gold);}
  .wordmark.on-dark{color:#fff;}

  .stripe{position:absolute;left:0;right:0;bottom:0;}
  .stripe .navy,.stripe .gold{position:absolute;top:0;bottom:0;}
  .stripe .navy{left:0;background:var(--navy);}
  .stripe .gold{right:0;background:var(--gold);}

  .icon{width:8px;height:8px;display:inline-block;vertical-align:-1px;margin-right:4px;}

  /* business card front */
  .card-front{left:55px;top:45px;width:266px;height:149px;background:var(--navy);display:flex;align-items:center;justify-content:center;}
  .card-front .wordmark{font-size:17px;}
  .card-front .mark{width:14px;height:14px;}

  /* business card back */
  .card-back{left:340px;top:45px;width:267px;height:149px;}
  .card-back .wordmark{position:absolute;left:14px;top:67px;font-size:11px;gap:4px;}
  .card-back .mark{width:9px;height:9px;}
  .card-back .divider{position:absolute;left:133px;top:35px;width:1px;height:77px;background:var(--navy);}
  .card-back .details{position:absolute;left:141px;top:34px;font-size:6.6px;line-height:10.4px;color:#333;}
  .card-back .name{font-family:'Lato',sans-serif;font-weight:700;font-size:10.5px;line-height:12px;color:var(--navy);}
  .card-back .name .first{color:var(--gold);}
  .card-back .gap{height:5px;}

  /* envelope front */
  .env-front{left:51px;top:215px;width:570px;height:261px;}
  .env-front .wordmark{position:absolute;left:40px;top:45px;font-size:18px;gap:8px;}
  .env-front .mark{width:15px;height:15px;}
  .env-front .return{position:absolute;left:40px;top:175px;font-size:9.3px;line-height:12.8px;color:#222;}
  .env-front .return .gap{height:4px;}
  .env-front .return .line{line-height:11.5px;}
  .env-front .watermark{position:absolute;left:370px;top:20px;width:200px;height:200px;border-radius:50%;background:#ebe9ef;}

  /* envelope back */
  .env-back{left:49px;top:492px;width:573px;height:266px;}
  .env-back .flap{position:absolute;left:0;top:0;width:573px;height:97px;}
  .env-back .wordmark{position:absolute;left:0;right:0;top:34px;justify-content:center;font-size:17px;}
  .env-back .mark{width:14px;height:14px;}

  /* letterhead */
  .letter{left:643px;top:43px;width:513px;height:715px;}
  .letter .wordmark{position:absolute;left:0;right:0;top:48px;justify-content:center;font-size:22px;gap:9px;}
  .letter .mark{width:18px;height:18px;}
  .letter .body{position:absolute;left:40px;width:430px;top:162px;font-size:10.2px;line-height:11.3px;color:#4a4a5a;}
  .letter .date{margin-bottom:13px;}
  .letter .block{margin-bottom:12px;}
  .letter .salutation{font-weight:700;font-size:12px;margin:2px 0 12px;}
  .letter p{text-align:justify;margin-bottom:11px;}
  .letter .regards{margin-top:25px;}
  .letter .signature{font-family:'Parisienne',cursive;font-size:25px;line-height:30px;color:#2a2a3a;margin-top:14px;}
  .letter .footer{position:absolute;left:36px;top:662px;display:flex;font-size:10.3px;line-height:14px;color:#333;}
  .letter .footer .col{padding:0 14px;border-left:1px solid var(--gold);}
  .letter .footer .col:first-child{padding-left:0;border-left:none;}
</style>
</head>
<body>

  <!-- business card front -->
  <div class="sheet card-front">
    <div class="wordmark on-dark"><span class="mark"></span>CEDAR &amp; VANE</div>
  </div>

  <!-- business card back -->
  <div class="sheet card-back">
    <div class="wordmark"><span class="mark"></span>CEDAR &amp; VANE</div>
    <div class="divider"></div>
    <div class="details">
      <div class="name"><span class="first">DANA</span> WHITLOW</div>
      <div>President</div>
      <div class="gap"></div>
      <div>Rue des Tilleuls 42</div>
      <div>CH-1004 Lausanne, Switzerland</div>
      <div class="gap"></div>
      <div><svg class="icon" viewBox="0 0 10 10"><path d="M2 1h2l1 2-1.2 1a5 5 0 0 0 2.2 2.2L7 5l2 1v2a1 1 0 0 1-1 1A7 7 0 0 1 1 2a1 1 0 0 1 1-1z" fill="var(--gold)"/></svg>+41 (0) 000 555 111</div>
      <div><svg class="icon" viewBox="0 0 10 10"><rect x="0.5" y="2" width="9" height="6" fill="var(--gold)"/><path d="M0.5 2l4.5 3.5L9.5 2" fill="none" stroke="#fff" stroke-width="0.8"/></svg>hello@cedarvane.com</div>
      <div><svg class="icon" viewBox="0 0 10 10"><circle cx="5" cy="5" r="4.5" fill="var(--gold)"/><path d="M0.5 5h9M5 0.5c-2 2.5-2 6.5 0 9M5 0.5c2 2.5 2 6.5 0 9" fill="none" stroke="#fff" stroke-width="0.6"/></svg>www.cedarvane.com</div>
    </div>
    <div class="stripe" style="height:5px;">
      <div class="navy" style="width:131px;clip-path:polygon(0 0,100% 0,calc(100% - 4px) 100%,0 100%);"></div>
      <div class="gold" style="left:131px;clip-path:polygon(4px 0,100% 0,100% 100%,0 100%);"></div>
    </div>
  </div>

  <!-- envelope front -->
  <div class="sheet env-front">
    <div class="watermark" aria-hidden="true"></div>
    <div class="wordmark"><span class="mark"></span>CEDAR &amp; VANE</div>
    <div class="return">
      <div>Rue des Tilleuls 42</div>
      <div>CH-1004 Lausanne, Switzerland</div>
      <div class="gap"></div>
      <div class="line"><svg class="icon" viewBox="0 0 10 10"><path d="M2 1h2l1 2-1.2 1a5 5 0 0 0 2.2 2.2L7 5l2 1v2a1 1 0 0 1-1 1A7 7 0 0 1 1 2a1 1 0 0 1 1-1z" fill="var(--gold)"/></svg>877-555-0142</div>
      <div class="line"><svg class="icon" viewBox="0 0 10 10"><rect x="0.5" y="2" width="9" height="6" fill="var(--gold)"/><path d="M0.5 2l4.5 3.5L9.5 2" fill="none" stroke="#fff" stroke-width="0.8"/></svg>hello@cedarvane.com</div>
      <div class="line"><svg class="icon" viewBox="0 0 10 10"><circle cx="5" cy="5" r="4.5" fill="var(--gold)"/><path d="M0.5 5h9M5 0.5c-2 2.5-2 6.5 0 9M5 0.5c2 2.5 2 6.5 0 9" fill="none" stroke="#fff" stroke-width="0.6"/></svg>www.cedarvane.com</div>
    </div>
    <div class="stripe" style="height:10px;">
      <div class="navy" style="width:362px;clip-path:polygon(0 0,100% 0,calc(100% - 8px) 100%,0 100%);"></div>
      <div class="gold" style="left:363px;clip-path:polygon(8px 0,100% 0,100% 100%,0 100%);"></div>
    </div>
  </div>

  <!-- envelope back -->
  <div class="sheet env-back">
    <svg class="flap" viewBox="0 0 573 97" preserveAspectRatio="none" aria-hidden="true">
      <path d="M0 0H573L560 70Q553 97 520 97H53Q20 97 13 70Z" fill="var(--navy)"/>
    </svg>
    <div class="wordmark on-dark"><span class="mark"></span>CEDAR &amp; VANE</div>
  </div>

  <!-- letterhead -->
  <div class="sheet letter">
    <div class="wordmark"><span class="mark"></span>CEDAR &amp; VANE</div>
    <div class="body">
      <div class="date">June -22-2020</div>
      <div class="block">Mr, Peter Lane<br>President</div>
      <div class="block">Northfield Group<br>123 Street Name, Suite# 10<br>City, State, 120023</div>
      <div class="salutation">Dear Mr, Peter</div>
      <p>Lorem ipsum dolor sit amet, consectetur adipisicing elit, sed do eiusmod tempor incididunt ut labore et dolore magna aliqua. Ut enim ad minim veniam, quis nostrud exercitation ullamco laboris nisi ut aliquip ex ea commodo consequat. Duis aute irure dolor in reprehenderit in voluptate velit esse cillum dolore eu fugiat nulla pariatur.</p>
      <p>Lorem ipsum dolor sit amet, consectetur adipisicing elit, sed do eiusmod tempor incididunt ut labore et dolore magna aliqua. Ut enim ad minim veniam, quis nostrud exercitation ullamco laboris nisi ut aliquip ex ea commodo consequat. Duis aute irure dolor in reprehenderit in voluptate velit esse cillum dolore eu fugiat nulla pariatur.</p>
      <p>Lorem ipsum dolor sit amet, consectetur adipisicing elit, sed do eiusmod tempor incididunt ut labore et dolore magna aliqua. Ut enim ad minim veniam, quis nostrud exercitation ullamco laboris nisi ut aliquip ex ea commodo consequat.</p>
      <p>Excepteur sint occaecat cupidatat non proident, sunt in culpa qui officia deserunt mollit anim id est laborum. re et dolore magnam aliquam quaerat voluptatem.</p>
      <div class="regards">Regards</div>
      <div class="signature">Adrian Hale</div>
    </div>
    <div class="footer">
      <div class="col">Street Name Ave, Suite 100<br>State name, Zip code, Country</div>
      <div class="col">
        <svg class="icon" viewBox="0 0 10 10"><path d="M2 1h2l1 2-1.2 1a5 5 0 0 0 2.2 2.2L7 5l2 1v2a1 1 0 0 1-1 1A7 7 0 0 1 1 2a1 1 0 0 1 1-1z" fill="var(--navy)"/></svg>+3 210 555 0167<br>
        <svg class="icon" viewBox="0 0 10 10"><rect x="2.5" y="0.5" width="5" height="3" fill="var(--navy)"/><rect x="0.5" y="3.5" width="9" height="4" fill="var(--navy)"/><rect x="2.5" y="6" width="5" height="3.5" fill="var(--navy)"/></svg>+3 210 555 0100
      </div>
      <div class="col">
        <svg class="icon" viewBox="0 0 10 10"><rect x="0.5" y="2" width="9" height="6" fill="var(--navy)"/><path d="M0.5 2l4.5 3.5L9.5 2" fill="none" stroke="#fff" stroke-width="0.8"/></svg>hello@cedarvane.com<br>
        <svg class="icon" viewBox="0 0 10 10"><circle cx="5" cy="5" r="4.5" fill="var(--navy)"/><path d="M0.5 5h9M5 0.5c-2 2.5-2 6.5 0 9M5 0.5c2 2.5 2 6.5 0 9" fill="none" stroke="#fff" stroke-width="0.6"/></svg>www.cedarvane.com
      </div>
    </div>
    <div class="stripe" style="height:10px;">
      <div class="navy" style="width:258px;clip-path:polygon(0 0,100% 0,calc(100% - 8px) 100%,0 100%);"></div>
      <div class="gold" style="left:259px;clip-path:polygon(8px 0,100% 0,100% 100%,0 100%);"></div>
    </div>
  </div>

</body>
</html>
```